Residential Roofing Company, need a Unique business card for a Woman owned ompany

Woman Owned Residential Roofing Company. Specializing in Insurance Claims
Attention to Detail is what sets this woman owned roofing company apart from the rest
We are QORVEL Certified and are an Accredited business with an A rating with the TMK. Our Contractor License number LTW38154

```html
<!DOCTYPE html>
<html lang="en">
<head>
<meta charset="utf-8">
<title>Crestline Roofing Business Card</title>
<link href="https://fonts.googleapis.com/css2?family=Lato:wght@400;700;900&display=swap" rel="stylesheet">
<style>
  :root {
    --page-bg: #d9d9d9;
    --card-bg: #1e1f20;
    --card-text: #ffffff;
    --muted-text: #c9c9c9;
    --rule: #8a8a8a;
    --badge-blue: #0a6fa6;
    --badge-blue-dark: #0b4f78;
    --badge-red: #e3141b;
    --badge-grey: #8c8c8c;
    --pattern-light: #3a3b3d;
    --pattern-dark: #161718;
  }
  * { box-sizing: border-box; margin: 0; padding: 0; }
  html, body { width: 1200px; height: 1108px; overflow: hidden; }
  body {
    background: var(--page-bg);
    font-family: "Lato", sans-serif;
    display: flex;
    align-items: center;
    justify-content: center;
    gap: 60px;
  }
  .card {
    width: 440px;
    height: 720px;
    background: var(--card-bg);
    border-radius: 22px;
    color: var(--card-text);
    position: relative;
    overflow: hidden;
    box-shadow: 0 10px 30px rgba(0,0,0,.25);
  }
  /* Brand wordmark */
  .brand-name {
    display: flex;
    align-items: center;
    justify-content: center;
    gap: 12px;
    font-weight: 900;
    font-size: 31px;
    letter-spacing: 1px;
    text-transform: uppercase;
    line-height: 1;
    white-space: nowrap;
  }
  .brand-mark {
    flex: none;
    width: 26px;
    height: 26px;
    border-radius: 50%;
    background: var(--card-text);
  }
  .brand-tagline {
    margin-top: 12px;
    font-size: 15px;
    font-weight: 700;
    letter-spacing: 1.5px;
    text-transform: uppercase;
    color: var(--muted-text);
  }
  /* Front */
  .card-front {
    display: flex;
    flex-direction: column;
    align-items: center;
    padding: 118px 40px 0;
    text-align: center;
  }
  .person-name {
    margin-top: 62px;
    font-weight: 700;
    font-size: 31px;
    letter-spacing: 1px;
    text-transform: uppercase;
  }
  .person-title {
    font-size: 21px;
    margin-top: 2px;
  }
  .icon-rule {
    display: flex;
    align-items: center;
    width: 290px;
    gap: 8px;
    margin-top: 12px;
  }
  .icon-rule .line { flex: 1; height: 1px; background: var(--rule); }
  .contact-icon {
    width: 30px; height: 30px;
    border: 2px solid var(--card-text);
    border-radius: 3px;
    display: flex; align-items: center; justify-content: center;
  }
  .contact-list, .address {
    font-size: 22px;
    line-height: 1.32;
    margin-top: 12px;
  }
  .rule {
    width: 300px;
    height: 1px;
    background: var(--rule);
    margin-top: 14px;
  }
  .badges {
    display: flex;
    gap: 18px;
    align-items: center;
    margin-top: 24px;
  }
  .badge-accredited {
    width: 175px; height: 66px;
    border-radius: 8px;
    background: linear-gradient(90deg, var(--badge-blue-dark) 0 38%, var(--badge-blue) 38%);
  }
  .badge-certified {
    width: 190px; height: 66px;
    border-radius: 4px;
    background: linear-gradient(180deg, var(--badge-grey) 0 30%, var(--badge-red) 30%);
  }
  /* Back */
  .pattern-field {
    position: absolute;
    inset: 0;
    background: linear-gradient(160deg, var(--pattern-light) 0%, var(--card-bg) 50%, var(--pattern-dark) 100%);
  }
  .back-brand {
    position: absolute;
    right: 40px;
    top: 470px;
    flex-direction: column;
    align-items: flex-end;
  }
  .back-brand .brand-name { font-size: 22px; gap: 10px; }
  .back-brand .brand-mark { width: 18px; height: 18px; }
  .back-brand .brand-tagline { font-size: 11px; margin-top: 8px; }
  .license {
    position: absolute;
    left: 70px;
    top: 580px;
    font-size: 24px;
    letter-spacing: .5px;
  }
</style>
</head>
<body>
  <section class="card card-front">
    <div class="brand-name"><span class="brand-mark"></span>Crestline Roofing</div>
    <p class="brand-tagline">Woman Owned · Insurance Claims</p>
    <h1 class="person-name">Daniel Harper</h1>
    <p class="person-title">Managing Director</p>
    <div class="icon-rule">
      <span class="line"></span>
      <span class="contact-icon">
        <svg width="18" height="18" viewBox="0 0 24 24" fill="#fff"><path d="M6.6 10.8a15 15 0 0 0 6.6 6.6l2.2-2.2a1 1 0 0 1 1-.25 11.4 11.4 0 0 0 3.6.57 1 1 0 0 1 1 1V20a1 1 0 0 1-1 1A17 17 0 0 1 3 4a1 1 0 0 1 1-1h3.5a1 1 0 0 1 1 1c0 1.250.2 2.45.57 3.57a1 1 0 0 1-.25 1z"/></svg>
      </span>
      <span class="contact-icon">
        <svg width="18" height="14" viewBox="0 0 24 18" fill="none" stroke="#fff" stroke-width="2"><rect x="1" y="1" width="22" height="16"/><path d="M1 1l11 9 11-9"/></svg>
      </span>
      <span class="contact-icon">
        <svg width="18" height="18" viewBox="0 0 24 24" fill="none" stroke="#fff" stroke-width="2"><circle cx="12" cy="12" r="10"/><path d="M2 12h20M12 2c3 3 3 17 0 20M12 2c-3 3-3 17 0 20"/></svg>
      </span>
      <span class="line"></span>
    </div>
    <p class="contact-list">055-987 321 640<br>hello@crestlinemail.com<br>www.crestlineroof.com</p>
    <div class="rule"></div>
    <p class="address">318, Harbor Lane<br>60714, Eastland</p>
    <div class="rule"></div>
    <div class="badges">
      <div class="badge-accredited" role="img" aria-label="TMK accredited business badge"></div>
      <div class="badge-certified" role="img" aria-label="QORVEL Certified contractor badge"></div>
    </div>
  </section>

  <section class="card card-back">
    <div class="pattern-field" role="img" aria-label="Repeating glossy brand pattern"></div>
    <div class="back-brand" style="display:flex">
      <div class="brand-name"><span class="brand-mark"></span>Crestline Roofing</div>
      <p class="brand-tagline">Woman Owned · Insurance Claims</p>
    </div>
    <p class="license">LIC NO. LTW38154</p>
  </section>
</body>
</html>
```